nukh almasira
nukh almasira - Corporate Services
Creative Brief
Simple
Kadhim Rubaie كاظم الربيعي
CEO المدير المفوض
Locality 482 - Alley 17 - House 8 Al Mansour - Baghdad - Iraq محلة 482 - زقاق 17 - دار 8 المنصور - بغداد - العراق
CEO@nukhalmasira.example
www.nukhalmasira.example
Concepts
Business Cards and Stationery for new compliance company.
Business Cards and Stationery for Background Check Company
qorvel42 qorvel42
good design but i hope you use the same name and information in the brief and if you can work on the logo cause i want to add the Arabic name of the company ( نخبة المسيرة ) if you can put the logo in the left and the name of the company in English and Arabic in the right of the logo and use the same font and size in Arabic and English name
Brisk Brisk
Ok
Please show me the whole stationary not only the business card
please use this e-mail on the letterhead only info@nukhalmasira.example and the address in arabic language use it only in the letterhead too thankyou

```html
<!DOCTYPE html>
<html lang="en">
<head>
<meta charset="utf-8">
<title>nukh almasira – Business Card</title>
<link href="https://fonts.googleapis.com/css2?family=Cairo:wght@400;500&family=Montserrat:wght@400;500&display=swap" rel="stylesheet">
<style>
  :root {
    --page-bg: #e9e9e6;
    --card-white: #ffffff;
    --brand-blue: #2f8fd3;
    --brand-orange: #f5a623;
    --ink-blue: #1c6fb5;
    --ink-grey: #3a3a3a;
    --text-light: #ffffff;
  }
  * { margin: 0; padding: 0; box-sizing: border-box; }
  html, body { width: 1200px; height: 901px; overflow: hidden; }
  body {
    background: var(--page-bg);
    font-family: "Montserrat", "Cairo", sans-serif;
    position: relative;
  }
  .business-card {
    position: absolute;
    left: 150px; top: 190px;
    width: 900px; height: 520px;
    background: var(--card-white);
    border-radius: 34px;
    overflow: hidden;
    box-shadow: 0 6px 22px rgba(0,0,0,0.12);
  }
  .card-shapes { position: absolute; inset: 0; }
  .brand-mark {
    position: absolute;
    left: 58px; top: 150px;
    display: flex; align-items: center; gap: 16px;
  }
  .brand-dot {
    width: 46px; height: 46px; border-radius: 50%;
    background: var(--brand-orange);
    flex: none;
  }
  .brand-names { display: flex; flex-direction: column; line-height: 1.25; }
  .brand-name {
    font-size: 26px; font-weight: 500;
    letter-spacing: 1px;
    color: var(--brand-orange);
    text-transform: uppercase;
  }
  .brand-name-ar { font-family: "Cairo", sans-serif; letter-spacing: 0; }
  .holder {
    position: absolute;
    left: 58px; top: 372px;
  }
  .holder-name {
    font-size: 27px; font-weight: 500;
    color: var(--ink-blue);
    text-transform: uppercase;
    letter-spacing: 1px;
  }
  .holder-role {
    margin-top: 6px;
    font-size: 20px; font-weight: 400;
    color: var(--ink-grey);
  }
  .holder-role-ar { font-family: "Cairo", sans-serif; }
  .contact-list {
    position: absolute;
    right: 42px; top: 72px;
    list-style: none;
    text-align: right;
    color: var(--text-light);
    font-size: 15px;
    line-height: 1.35;
  }
  .contact-list li { display: flex; justify-content: flex-end; align-items: center; gap: 10px; }
  .contact-list .address { display: block; margin-bottom: 30px; }
  .contact-list .gap { margin-top: 12px; }
  .contact-icon { width: 15px; height: 15px; flex: none; }
</style>
</head>
<body>
  <section class="business-card" aria-label="Business card front">
    <svg class="card-shapes" viewBox="0 0 900 520" preserveAspectRatio="none" aria-hidden="true">
      <path d="M690 0 C750 40 820 50 900 40 L900 0 Z" fill="var(--brand-orange)"/>
      <path d="M582 0 C507 130 562 270 442 400 C402 450 362 490 337 520 L375 520 C400 490 440 450 480 400 C600 270 545 130 620 0 Z" fill="var(--brand-orange)"/>
      <path d="M620 0 C545 130 600 270 480 400 C440 450 400 490 375 520 L900 520 L900 58 C820 70 750 60 690 20 L670 0 Z" fill="var(--brand-blue)"/>
      <path d="M609 0 C534 130 589 270 469 400 C429 450 389 490 364 520" fill="none" stroke="var(--card-white)" stroke-width="3"/>
    </svg>

    <div class="brand-mark">
      <span class="brand-dot"></span>
      <div class="brand-names">
        <span class="brand-name">nukh almasira</span>
        <span class="brand-name brand-name-ar" lang="ar" dir="rtl">نخبة المسيرة</span>
      </div>
    </div>

    <div class="holder">
      <p class="holder-name">Kadhim Rubaie</p>
      <p class="holder-role">CEO · <span class="holder-role-ar" lang="ar">المدير المفوض</span></p>
    </div>

    <ul class="contact-list">
      <li class="address">Locality 482 - Alley 17<br>House 8 - Al Mansour<br>Baghdad - Iraq</li>
      <li>010 482 1735
        <svg class="contact-icon" viewBox="0 0 16 16"><path d="M3 1 L6 1 L7 5 L5 6 C6 8 8 10 10 11 L11 9 L15 10 L15 13 C15 14 14 15 13 15 C6 15 1 10 1 3 C1 2 2 1 3 1 Z" fill="currentColor"/></svg>
      </li>
      <li class="gap">010 482 1735
        <svg class="contact-icon" viewBox="0 0 16 16"><rect x="4" y="1" width="8" height="14" rx="1.5" fill="none" stroke="currentColor" stroke-width="1.6"/><circle cx="8" cy="12.5" r="0.9" fill="currentColor"/></svg>
      </li>
      <li class="gap">010 482 1735
        <svg class="contact-icon" viewBox="0 0 16 16"><rect x="1" y="6" width="14" height="8" rx="1" fill="currentColor"/><rect x="4" y="2" width="8" height="5" fill="none" stroke="currentColor" stroke-width="1.4"/></svg>
      </li>
      <li class="gap">CEO@nukhalmasira.example
        <svg class="contact-icon" viewBox="0 0 16 16"><rect x="1" y="3" width="14" height="10" rx="1" fill="none" stroke="currentColor" stroke-width="1.5"/><path d="M1.5 3.5 L8 9 L14.5 3.5" fill="none" stroke="currentColor" stroke-width="1.5"/></svg>
      </li>
      <li class="gap">www.nukhalmasira.example
        <svg class="contact-icon" viewBox="0 0 16 16"><circle cx="8" cy="8" r="6.5" fill="none" stroke="currentColor" stroke-width="1.4"/><ellipse cx="8" cy="8" rx="3" ry="6.5" fill="none" stroke="currentColor" stroke-width="1.2"/><path d="M1.5 8 H14.5" stroke="currentColor" stroke-width="1.2"/></svg>
      </li>
    </ul>
  </section>
</body>
</html>
```